Selbsthilfegruppe für organtransplantierte Personen sucht Flyer-Design
Sehr schnelle Reaktion auf Änderungswünsche und top Support bis zum Druck :) Gerne wieder!
Zielgruppe
Wir sind eine Selbsthilfegruppe für organtransplantierte Personen, Zielgruppe sind Personen aus der Region die auch ein Spenderorgan empfangen haben und deren Angehörige, die Beistand und Information suchen sowie gemeinsame Aktivitäten wahrnehmen möchten.
Aufgabenstellung
Es gibt bereits einen Flyer der jedoch überarbeitet und etwas schöner und moderner gestaltet werden soll. Der Text kann bestehen bleiben und die Aufteilung muss nicht zwingend geändert werden, anstelle der aktuellen Fotos sollen dann andere eingefügt werden, die übergeben werden, sobald das Design akzeptiert wurde. Es geht hauptsächlich um das Design selbst, es soll ansprechen, freundlich, modern und hoffnungsvoll sein, die Grundfarbe sollte grün sein. Das Logo kann beibehalten aber farblich auch gerne angepasst werden. Es soll ein normaler Faltflyer sein, 2 Faltungen und damit vorn und hinten je 3 einzelne Bereiche wie aktuell, Gesamtmaß A4. Bei Rückfragen gerne melden!

```html
<!DOCTYPE html>
<html lang="de">
<head>
<meta charset="utf-8">
<title>Miteinander Stark – Flyer Innenseite</title>
<link rel="stylesheet" href="https://fonts.googleapis.com/css2?family=Raleway:wght@400;600&family=Pinyon+Script&display=swap">
<style>
  :root {
    --green: #5a9e3c;
    --green-light: #6fb34c;
    --green-deep: #4a8a2f;
    --white: #ffffff;
    --backdrop: #b9babd;
  }
  * { margin: 0; padding: 0; box-sizing: border-box; }
  html, body { width: 1200px; height: 675px; overflow: hidden; }
  body {
    background: var(--backdrop);
    font-family: "Raleway", Arial, sans-serif;
    color: var(--green);
    position: relative;
  }
  ul { list-style: none; }
  .flyer {
    position: absolute;
    left: 137px; top: 10px;
    width: 926px; height: 654px;
    background: var(--white);
    overflow: hidden;
  }
  .flyer-shapes { position: absolute; inset: 0; z-index: 0; }
  .benefit, .support-item {
    position: absolute;
    z-index: 1;
    font-size: 15px;
    line-height: 19px;
  }
  .benefit { left: 39px; }
  .support-item { left: 330px; font-size: 16px; line-height: 20px; }
  .benefit::before, .support-item::before {
    content: "";
    position: absolute;
    left: -18px; top: 50%;
    width: 10px; height: 10px;
    margin-top: -5px;
    border-radius: 50%;
    background: var(--green);
  }
  .contact-title {
    position: absolute;
    left: 305px; top: 34px; width: 200px;
    text-align: center;
    font-family: "Pinyon Script", cursive;
    font-weight: 400;
    font-size: 38px;
    line-height: 40px;
  }
  .contact-title span { border-bottom: 1px solid var(--green); padding: 0 2px; }
  .contact-photo {
    position: absolute;
    left: 336px; top: 84px;
    width: 162px; height: 162px;
    border-radius: 50%;
    border: 2px solid var(--green);
    background: radial-gradient(circle at 50% 45%, #e9cdb4 0%, #bfa08a 45%, #f3f3f3 75%);
  }
  .contact-heading {
    position: absolute;
    left: 317px; top: 256px;
    font-size: 15px; font-weight: 600;
    line-height: 20px;
    padding-bottom: 2px;
    border-bottom: 1px solid var(--green);
  }
  .support-intro {
    position: absolute;
    left: 330px; top: 296px;
    font-size: 16px;
  }
  .brand {
    position: absolute;
    left: 617px; top: 26px; width: 309px;
    text-align: center;
  }
  .brand-mark {
    display: block;
    width: 44px; height: 44px;
    margin: 0 auto 40px;
    border-radius: 50%;
    border: 3px solid var(--green);
  }
  .brand-name {
    display: inline-block;
    font-size: 26px;
    font-weight: 400;
    line-height: 30px;
    border-bottom: 1px solid var(--green);
    padding: 0 4px 2px;
  }
  .brand-sub {
    margin-top: 6px;
    font-size: 16px;
    line-height: 20px;
  }
  .offer {
    position: absolute;
    z-index: 1;
    left: 617px; top: 549px; width: 309px;
    text-align: center;
    color: var(--white);
    font-size: 18px;
    line-height: 24px;
  }
</style>
</head>
<body>
  <main class="flyer">
    <svg class="flyer-shapes" width="926" height="654" viewBox="0 0 926 654">
      <defs>
        <linearGradient id="band" x1="0" y1="0" x2="0" y2="1">
          <stop offset="0" stop-color="#6fb34c"/>
          <stop offset="1" stop-color="#4a8a2f"/>
        </linearGradient>
        <radialGradient id="groupTone" cx="0.5" cy="0.6" r="0.6">
          <stop offset="0" stop-color="#b89a82"/>
          <stop offset="0.55" stop-color="#cfd3d8"/>
          <stop offset="1" stop-color="#eef0f2"/>
        </radialGradient>
        <clipPath id="photoClip">
          <path d="M621 187 H926 V418 C860 458 760 490 680 512 H621 Z"/>
        </clipPath>
      </defs>
      <path d="M0 0 H431 C260 28 90 72 0 118 Z" fill="url(#band)"/>
      <g clip-path="url(#photoClip)">
        <circle cx="776" cy="342" r="155" fill="url(#groupTone)" role="img" aria-label="Foto einer fröhlichen Gruppe von Menschen, die jubeln"/>
      </g>
      <path d="M621 342 A155 155 0 0 1 926 300" fill="none" stroke="#5a9e3c" stroke-width="2.5"/>
      <path d="M0 596 C250 566 450 536 617 512 C750 492 860 458 926 418 V654 H0 Z" fill="url(#band)"/>
    </svg>

    <ul class="benefits">
      <li class="benefit" style="top:119px">Suchen und Finden von<br>Gleichgesinnten</li>
      <li class="benefit" style="top:174px">Einsamkeit durch Gemeinsamkeit<br>überwinden</li>
      <li class="benefit" style="top:230px">Lebenssituation verbessern</li>
      <li class="benefit" style="top:266px">Beziehungen aufbauen<br>und verbessern</li>
      <li class="benefit" style="top:321px">Schwierigkeiten zusammen<br>meistern</li>
      <li class="benefit" style="top:378px">Teilnehmen und verstehen</li>
      <li class="benefit" style="top:415px">Handeln in eigener Sache</li>
      <li class="benefit" style="top:452px">Informationen geben</li>
      <li class="benefit" style="top:489px">Lösungen entdecken und entwickeln</li>
      <li class="benefit" style="top:525px">Freude am Leben finden:<br>Jetzt erst recht!</li>
    </ul>

    <h2 class="contact-title"><span>Kontakt:</span></h2>
    <div class="contact-photo" role="img" aria-label="Porträtfoto einer Ansprechpartnerin mit Headset"></div>
    <h3 class="contact-heading">Info zum Ansprechpartner:</h3>
    <p class="support-intro">Wir werden unterstützt</p>
    <ul class="support">
      <li class="support-item" style="top:334px">von der Stiftung Lebensbrücke<br>(SLB)</li>
      <li class="support-item" style="top:394px">vom Klinikum Bad Lindental: MVZ</li>
      <li class="support-item" style="top:433px">von Fachärzten aus dem Bereich<br>Innere Medizin</li>
      <li class="support-item" style="top:492px">vom Frauenzentrum „Marlene“<br>in Bad Lindental</li>
    </ul>

    <header class="brand">
      <span class="brand-mark"></span>
      <h1 class="brand-name">Miteinander Stark</h1>
      <p class="brand-sub">Selbsthilfegruppe<br>für Organtransplatation</p>
    </header>

    <p class="offer">Wir bieten Hilfe für Betroffene<br>sowie Angehörige im Raum Bad<br>Lindental an</p>
  </main>
</body>
</html>
```